Need Landing Page for Data Security Company

Need a new landing page (PSD) for our data security company (www.korvalim.com). We specialize in selling patented hard drive destruction machines that guarantee the data on your hard drives are unrecoverable. We have several large clients such as Trellio, Quibblr and Marquell just to name a few. Really want to have a landing page that sticks out.

Attached is a one pager we use just for emailing clients. We do not want the landing page to look like this. This is just for content to read. The landing page needs

Target Market(s)

Government, business corporations, IT decision makers. Not every day user

Industry/Entity Type

It Company

Number of Pages Required

1 page

Font styles to use
Other font styles liked:
• Match Current Website

Requirements
Must have
• Its a landing page so it needs a Contact us Section at the very top!!!
• Need to be a very attractive landing page.. Would like a mix of showcasing our products and also having some client list to show our bigger name clients (trellio, marquell, quibblr)
• Landing page needs to use the same color/style schema as current website. Also will be using the same menu structure as what exists today.
• www.korvalim.com
Nice to have
• Maybe some vidmora videos of our products?

```html
<!DOCTYPE html>
<html lang="en">
<head>
<meta charset="utf-8">
<title>Korvalim Technologies – Data Destruction</title>
<link href="https://fonts.googleapis.com/css2?family=Roboto:wght@300;400;500;700&family=Roboto+Slab:wght@400;700&display=swap" rel="stylesheet">
<style>
:root{
  --green:#8cc63f;
  --green-dark:#74ad2c;
  --orange:#f26522;
  --ink:#333;
  --muted:#777;
  --topbar:#1c1c1c;
  --grey-bg:#ececec;
  --line:#d6d6d6;
  --clients:#2c3b4a;
  --footer:#1f2c39;
  --copy:#141c24;
  --white:#fff;
}
*{box-sizing:border-box;margin:0;padding:0}
html,body{width:1200px;height:2452px;overflow:hidden}
body{font-family:"Roboto",Arial,sans-serif;color:var(--ink);background:var(--white);position:relative}
.slab{font-family:"Roboto Slab",Georgia,serif}

/* top bar */
.topbar{height:80px;background:var(--topbar);position:relative}
.brand{position:absolute;left:150px;top:20px;display:flex;align-items:center;gap:10px;color:var(--white);font-weight:700;font-size:28px}
.brand .dot{width:14px;height:14px;border-radius:50%;background:var(--green)}
.brand small{display:block;font-size:9px;font-weight:400;color:#aaa;letter-spacing:1px}
.phone{position:absolute;right:150px;top:14px;display:flex;align-items:center;gap:8px;color:var(--white);font-size:18px;font-weight:500}
.nav{position:absolute;right:150px;top:52px;display:flex;gap:24px;font-size:10px;color:var(--white);font-weight:500;letter-spacing:.5px}

/* hero */
.hero{height:300px;background:linear-gradient(180deg,#93cb46,#84bd37);text-align:center;color:var(--white);padding-top:62px}
.hero h1{font-family:"Roboto Slab",serif;font-weight:400;font-size:30px;letter-spacing:1px}
.hero p{font-size:20px;font-weight:300;margin-top:10px}
.hero-form{display:flex;justify-content:center;gap:8px;margin-top:26px}
.hero-form .field{width:160px;height:30px;background:var(--white);border-radius:2px;color:#aaa;font-size:11px;text-align:left;padding:9px 10px}
.hero-form .btn{width:76px;height:30px;background:var(--orange);border-radius:2px;font-size:11px;font-weight:700;padding-top:9px}

/* showcase */
.showcase{position:relative;height:240px}
.item{position:absolute;top:-70px;width:240px;text-align:center}
.item .disc{width:170px;height:170px;margin:0 auto;border-radius:50%;border:6px solid var(--white);box-shadow:0 0 0 1px var(--line)}
.item h3{color:var(--green);font-size:16px;font-weight:700;margin-top:18px;line-height:1.25}
.arrow{position:absolute;top:10px}

/* about */
.about{padding:10px 100px 0;height:220px}
.about h2{font-family:"Roboto Slab",serif;text-align:center;font-size:24px;color:#555;font-weight:700;margin-bottom:22px}
.about p{font-size:12px;line-height:1.7;color:var(--muted);margin-bottom:12px}
.about p.lead{color:var(--ink);font-weight:500}

/* products */
.products{background:var(--grey-bg);height:680px;padding:44px 150px 0;position:relative}
.products h2{font-family:"Roboto Slab",serif;color:var(--green);font-size:22px;font-weight:700;margin-bottom:32px}
.product-menu{position:absolute;left:150px;top:120px;width:290px;list-style:none}
.product-menu li{height:42px;border:1px solid var(--line);border-top:none;background:var(--white);font-size:11px;font-weight:500;padding:14px 16px;color:#555;display:flex;align-items:center;gap:10px}
.product-menu li:first-child{border-top:1px solid var(--line)}
.product-menu li.active{background:var(--green);color:var(--white);border-color:var(--green)}
.product-menu li::before{content:"";width:6px;height:6px;border-radius:50%;background:currentColor}
.product-detail{position:absolute;left:480px;top:120px;width:570px}
.product-detail h3{font-family:"Roboto Slab",serif;font-size:20px;color:#444;margin-bottom:16px}
.product-detail p{font-size:12px;line-height:1.7;color:var(--muted)}
.video{margin-top:26px;height:260px;background:#050505;position:relative;color:var(--white)}
.video .title{position:absolute;left:0;right:0;top:100px;text-align:center;font-size:28px;font-weight:700}
.video .title span{display:block;font-size:10px;font-weight:400;color:#aaa;margin-top:4px}
.video .bar{position:absolute;left:0;right:0;bottom:0;height:26px;background:#222;display:flex;align-items:center;padding:0 10px;gap:10px}
.video .track{flex:1;height:4px;background:#555;position:relative}
.video .track i{position:absolute;left:0;top:0;width:30%;height:4px;background:var(--green)}

/* signup */
.signup{height:520px;padding-top:60px;text-align:center}
.signup h2{font-family:"Roboto Slab",serif;font-size:24px;color:#555;font-weight:700;margin-bottom:36px}
.signup-form{width:620px;margin:0 auto;display:grid;grid-template-columns:1fr 1fr;gap:14px 20px;text-align:left}
.signup-form .field{height:34px;background:#e4e4e4;font-size:11px;color:#888;padding:11px 12px}
.signup-form .area{grid-column:1/3;height:170px}
.signup-form .btn{grid-column:2/3;justify-self:end;width:100px;height:30px;background:var(--green);color:var(--white);font-size:11px;font-weight:700;text-align:center;padding-top:9px}

/* clients */
.clients{height:120px;background:var(--clients);display:flex;align-items:center;justify-content:center;gap:56px;color:var(--white)}
.clients .name{font-size:30px;font-weight:700;color:#e6e9ec}
.clients .chev{font-size:28px;color:#aeb8c2}

/* footer */
.footer{height:260px;background:var(--footer);padding:40px 150px 0;display:flex;gap:40px;color:#a9b4bf;font-size:10px}
.footer .brand-f{width:220px;color:var(--white);font-size:26px;font-weight:700;display:flex;align-items:center;gap:10px;align-self:flex-start;margin-top:40px}
.footer .brand-f .dot{width:12px;height:12px;border-radius:50%;background:var(--green)}
.footer .col{width:150px}
.footer h4{color:var(--white);font-size:11px;font-weight:700;margin-bottom:12px;letter-spacing:.5px}
.footer li{list-style:none;line-height:1.9}
.social{display:flex;gap:8px;margin-top:12px}
.social span{width:24px;height:24px;border-radius:50%;border:1px solid #7d8a96}
.copyright{height:52px;background:var(--copy);color:#7d8a96;font-size:10px;padding:20px 150px}
</style>
</head>
<body>

<header class="topbar">
  <div class="brand"><span class="dot"></span><div>Korvalim<small>DATA DESTRUCTION</small></div></div>
  <div class="phone">
    <svg width="16" height="16" viewBox="0 0 24 24"><path fill="#8cc63f" d="M6.6 10.8a15 15 0 0 0 6.6 6.6l2.2-2.2a1 1 0 0 1 1-.25 11.4 11.4 0 0 0 3.6.57 1 1 0 0 1 1 1V20a1 1 0 0 1-1 1A17 17 0 0 1 3 4a1 1 0 0 1 1-1h3.5a1 1 0 0 1 1 1c0 1.25.2 2.45.57 3.57a1 1 0 0 1-.25 1z"/></svg>
    555-014-2290
  </div>
  <nav class="nav"><span>HOME</span><span>ABOUT US</span><span>PRODUCTS</span><span>SERVICES</span><span>COMPLIANCE</span><span>BLOG</span><span>CONTACT</span></nav>
</header>

<section class="hero">
  <h1>DUIS AUTEM VEL EUM IRIURE DOLOR</h1>
  <p>Keep live inventory, update sales and more!</p>
  <div class="hero-form">
    <div class="field">First Name</div><div class="field">Last Name</div><div class="field">Email</div><div class="field">Phone</div><div class="btn">SUBMIT</div>
  </div>
</section>

<section class="showcase">
  <div class="item" style="left:180px">
    <div class="disc" role="img" aria-label="Hard drive and disc storage media" style="background:radial-gradient(circle,#dcdcdc,#9a9a9a)"></div>
    <h3>COMPUTER STORAGE<br>MEDIA</h3>
  </div>
  <svg class="arrow" style="left:395px" width="90" height="40" viewBox="0 0 90 40"><path d="M5 30 Q45 0 80 26" fill="none" stroke="#999" stroke-width="2"/><path d="M72 20 L82 28 L70 31" fill="none" stroke="#999" stroke-width="2"/></svg>
  <div class="item" style="left:480px">
    <div class="disc" role="img" aria-label="Shredlock destroyer machine" style="background:radial-gradient(circle,#f4f4f4,#bdbdbd)"></div>
    <h3>KORVALIM SHREDLOCK<br>DESTROYER</h3>
  </div>
  <svg class="arrow" style="left:695px" width="90" height="40" viewBox="0 0 90 40"><path d="M5 30 Q45 0 80 26" fill="none" stroke="#999" stroke-width="2"/><path d="M72 20 L82 28 L70 31" fill="none" stroke="#999" stroke-width="2"/></svg>
  <div class="item" style="left:780px">
    <div class="disc" role="img" aria-label="Pile of destroyed drive fragments" style="background:radial-gradient(circle,#8a8a8a,#3c3c3c)"></div>
    <h3>KORVALIM SHREDLOCK<br>DESTROYER</h3>
  </div>
</section>

<section class="about">
  <h2>ABOUT KORVALIM TECHNOLOGIES</h2>
  <p class="lead">Korvalim Technologies, Inc. is a privately held technology research and development company dedicated to engineering innovative solutions in information technology, energy and the environmental field.</p>
  <p>Our company is focused on data security: we design, build and support patented hard drive destruction machines that make stored data permanently unrecoverable. Every unit is tested in house and backed by our support team, so government agencies and corporations can retire media with confidence. Our systems meet current disposal standards and are trusted by IT decision makers worldwide for secure, verified and fast destruction on site.</p>
</section>

<section class="products">
  <h2>KORVALIM PRODUCTS</h2>
  <ul class="product-menu">
    <li class="active">ABOUT US</li>
    <li>SHREDLOCK COMPACT</li>
    <li>SHREDLOCK</li>
    <li>SHREDLOCK SSD</li>
    <li>SHREDLOCK COMPACT SSD</li>
    <li>V-LOCK SSD</li>
    <li>SHREDLOCK WORKSHOP</li>
  </ul>
  <div class="product-detail">
    <h3>SHREDLOCK</h3>
    <p>The Shredlock with no fixtures or adjustments required, crushing any 3.5" hard drive in under 10 seconds and destroying the platters beyond any recovery method. It is designed for secure office environments where drives must be destroyed on site, with quiet operation and simple one button control. The built in counter logs every drive processed.</p>
    <div class="video">
      <div class="title">Korvalim<span>DATA DESTRUCTION</span></div>
      <div class="bar">
        <svg width="10" height="12" viewBox="0 0 10 12"><path d="M0 0 L10 6 L0 12z" fill="#fff"/></svg>
        <div class="track"><i></i></div>
        <span style="font-size:10px">0:42</span>
      </div>
    </div>
  </div>
</section>

<section class="signup">
  <h2>INTERESTED? SIGN UP!</h2>
  <div class="signup-form">
    <div class="field">Name</div><div class="field">Phone</div>
    <div class="field">Email</div><div class="field">Subject</div>
    <div class="field area">Tell us about your requirements</div>
    <div class="btn">SUBMIT</div>
  </div>
</section>

<section class="clients">
  <span class="chev">‹</span>
  <span class="name">trellio</span>
  <span class="name">marquell</span>
  <span class="name">Veridane</span>
  <span class="name">quibblr</span>
  <span class="name">Orbitrax</span>
  <span class="chev">›</span>
</section>

<footer class="footer">
  <div class="brand-f"><span class="dot"></span>Korvalim</div>
  <div class="col"><h4>QUICK LINKS</h4><ul><li>Home</li><li>About Us</li><li>Products</li><li>Services</li><li>Compliance</li><li>Blog</li><li>Contact</li></ul></div>
  <div class="col"><h4>PRODUCTS</h4><ul><li>Shredlock Compact</li><li>Shredlock</li><li>Shredlock SSD</li><li>Compact SSD</li><li>V-Lock SSD</li><li>Shredlock Workshop</li></ul></div>
  <div class="col"><h4>CONTACT</h4><ul><li>1200 Harbor Lane</li><li>Suite 40, Bayview</li><li>555-014-2290</li><li>info@korvalim.com</li><li>www.korvalim.com</li></ul></div>
  <div class="col" style="width:190px"><h4>FOLLOW US</h4><ul><li>Follow us for product news, updates and video demos on vidmora.</li></ul>
    <div class="social"><span></span><span></span><span></span></div></div>
</footer>
<div class="copyright">Copyright © 2024 Korvalim Technologies. All Rights Reserved.</div>

</body>
</html>
```